The Next Wavelet Online Radio!

We need a LANDING PAGE that is fun, light hearted, and has elements related to the themes of "music" "concerts" "radio". Think marquis; juke box; record player or old radio; people listening to or jamming out to music, play buttons, neon lights, chrome, stages. (none required, just ideas). The site could be retro, or modern, or anything you dream up.

The winning designer will likely get more work in the future. Probably others who make submissions, too.

The company, TuneKiosk.com, makes free internet radio stations that are named/branded after LOCAL MUSIC CLUBS AND FESTIVALS worldwide. Attached are actual banners for a bunch of these stations.

We need a way to incorporate a group of THESE VERY BANNERS (and maybe some associated station information) within a single landing page, where users get to choose from a selection of them. Think: a menu of stations. So the user thinks to them self: "OK, I'm seeing four (or six, or ten) radio stations, which should I choose?".

To see for yourself how TuneKiosk works, go here and launch some stations: http://tunekiosk-example.com/partners

(note, these are not the graphics to use for this web design project, please use the attached banners.

Note: there should be a way for users to push PLAY for each selectable station, AND a separate way for them to FOLLOW stations. On TuneKiosk, following us indicated by a STAR icon.

When a user has followed (starred) a station, then that station goes into their list of present stations, for quick-play in future.

Project Deadline Extended
Reason: Several designers are still working on revisions, so we are extending the deadline so they have time to make necessary changes. Feedback will be sent today to ALL submissions. -ws

Target Market(s)

Our customers are listeners to internet radio. Our site should make it easy for them to a) understand that these attached banners are:
1) playable radio channels
2) follow-able

Industry/Entity Type

Internet

Font styles to use
Sans Serif

Requirements
Nice to have
• The banners can have corners rounded, or be altered, textured, "wrapped around".... don't be limited by their uniformity.

```html
<!DOCTYPE html>
<html lang="en">
<head>
<meta charset="utf-8">
<title>TuneKiosk – Landing</title>
<link href="https://fonts.googleapis.com/css2?family=Questrial&family=Roboto:wght@400;500;700&display=swap" rel="stylesheet">
<style>
:root{
  --teal:#15b3a6;
  --teal-bright:#14d2b8;
  --teal-deep:#0b6a6d;
  --teal-mid:#137c80;
  --teal-soft:#7adcd6;
  --teal-pale:#8ee3dc;
  --cyan:#3cc7d4;
  --ink:#0f4a5a;
  --grey:#555;
  --line:#d9d9d9;
  --white:#fff;
}
*{margin:0;padding:0;box-sizing:border-box}
html,body{width:1000px;height:1200px;overflow:hidden;background:var(--white)}
body{font-family:"Questrial",sans-serif;color:var(--grey);position:relative}
.abs{position:absolute}

/* header */
.logo{left:270px;top:11px;display:flex;align-items:center;gap:5px;color:var(--teal);font-family:"Roboto",sans-serif;font-weight:700;font-size:19px}
.logo-dot{width:22px;height:22px;border-radius:50%;border:2px solid var(--teal)}
.nav{right:265px;top:16px;font-size:10px;color:#555;display:flex;gap:8px}

/* hero */
.hero{left:196px;top:44px;width:610px;height:244px;background:linear-gradient(100deg,#12a597 0%,#13bfae 55%,#14d4ba 100%)}
.hero svg{position:absolute;left:100px;top:20px}
.hero-title{left:305px;top:135px;color:var(--white);font-size:13px;letter-spacing:.3px}
.hero-sub{left:306px;top:150px;color:#dff7f3;font-size:7.5px}
.join{left:306px;top:173px;width:77px;height:21px;background:#53d9c6;display:flex;align-items:center;font-size:9px;color:var(--white)}
.join i{width:21px;height:21px;background:#0f8c86;display:flex;align-items:center;justify-content:center;margin-right:10px}

/* carousel */
.arrow{top:352px;color:#f2c7cf;font-size:12px}
.card{top:312px;width:95px}
.card .art{width:95px;height:95px;position:relative}
.card h3{font-family:"Roboto",sans-serif;font-weight:500;font-size:10.5px;color:var(--teal);text-align:center;margin-top:5px;height:17px}
.card hr{border:0;border-top:1px solid var(--line);margin-top:1px}
.stars{text-align:center;font-size:9px;letter-spacing:1px;margin-top:3px;color:var(--ink)}
.stars .off{color:#9fd6d8}
.mini-player{position:absolute;left:-4px;top:41px;width:103px;height:52px;background:rgba(40,40,50,.85);color:#fff;font-family:"Roboto",sans-serif}
.mini-player .label{position:absolute;left:6px;bottom:8px;font-size:5px;font-weight:700}
.mini-player .time{position:absolute;right:7px;bottom:8px;font-size:5.5px;color:#e8d24c}

/* top 3 */
.top3{left:279px;top:466px;width:168px;height:154px;background:var(--cyan);font-family:"Roboto",sans-serif}
.rank{position:absolute;left:0;width:22px;height:41px;background:#6adbd8;color:#fff;font-size:8px;display:flex;align-items:center;justify-content:center}
.track{position:absolute;left:22px;width:146px;height:41px;border-bottom:1px solid #5ad4de}
.track .thumb{position:absolute;left:10px;top:7px;width:27px;height:27px;border-radius:50%}
.track b{position:absolute;left:43px;top:11px;font-size:9px;font-weight:500;color:var(--ink)}
.track small{position:absolute;left:43px;top:23px;font-size:4.5px;color:#e8fbfd}
.track em{position:absolute;right:8px;top:16px;font-size:5px;font-style:normal;color:#e8fbfd}
.top3-foot{position:absolute;left:0;top:123px;width:168px;height:31px}
.top3-label{position:absolute;left:5px;top:14px;font-size:17px;font-weight:700;color:#7fe3e6;letter-spacing:.5px}
.tab-btn{position:absolute;top:0;width:50px;height:31px;color:#fff;font-size:7px;text-align:center;padding-top:18px}

/* video */
.video{left:478px;top:466px;width:242px;height:154px;background:linear-gradient(135deg,#b9a8b4 0%,#e6d2d0 40%,#9d6d78 70%,#6a5a74 100%)}
.video-bar{position:absolute;left:0;bottom:0;width:242px;height:30px;background:rgba(120,100,130,.75);color:#fff;font-family:"Roboto",sans-serif;font-size:7px}

/* station panel */
.panel{left:196px;top:657px;width:610px;height:420px;background:linear-gradient(110deg,#0a6265 0%,#0c7a7b 50%,#11a39a 100%)}
.ptab{position:absolute;top:0;height:81px;color:#fff;font-size:8.5px;text-align:center}
.ptab span{position:absolute;left:0;right:0;bottom:9px}
.ptab svg{position:absolute;left:50%;transform:translateX(-50%);top:18px}

.side{position:absolute;left:21px;width:82px;font-size:6px;color:#fff}
.side-head{height:22px;display:flex;align-items:center;background:#137e84;font-size:11px}
.side-head i{width:22px;height:22px;background:#0f6a70;display:flex;align-items:center;justify-content:center;margin-right:8px}
.side-item{height:20px;display:flex;align-items:center;background:#117a80;border-top:1px solid #0d686d;position:relative}
.side-item::before{content:"";width:4px;height:4px;border-radius:50%;background:#fff;margin:0 8px 0 4px}
.side-item i{position:absolute;left:11px;top:0;width:1px;height:20px;background:#0d686d}
.side-btn{height:11px;margin-top:3px;background:#137e84;text-align:center;line-height:11px;font-size:5.5px}
.side-rule{height:1px;background:#0a5558;margin:10px 10px}
.find{position:absolute;left:31px;top:368px;width:62px;height:17px;background:var(--teal-bright);color:#fff;font-size:8px;font-family:"Roboto",sans-serif;font-weight:700;display:flex;align-items:center;justify-content:center}

.gigs{position:absolute;left:150px;top:103px;width:439px;height:282px}
.gigs-head{position:absolute;left:0;top:0;width:439px;height:52px;background:var(--teal-soft)}
.gigs-head .lead{position:absolute;left:0;top:0;width:31px;height:52px;background:#6cd0ca}
.gigs-head h4{position:absolute;top:30px;font-weight:400;font-size:15px;color:#1d9ba0}
.row{position:absolute;left:0;width:431px;height:32px;background:var(--teal-soft);border-top:1px solid #4fb8b4;font-family:"Roboto",sans-serif}
.row .star{position:absolute;left:0;top:0;width:31px;height:31px;background:#6cd0ca;color:var(--ink);font-size:9px;text-align:center;line-height:31px}
.row .star.off{color:#fff}
.row b{position:absolute;left:41px;top:9px;font-size:10.5px;font-weight:500;color:var(--ink)}
.row small{position:absolute;left:41px;top:21px;font-size:4.5px;color:#2e7f85}
.row .gig{left:207px}
.scroll{position:absolute;left:431px;top:54px;width:8px;height:228px;background:#0c7f82}
.scroll i{position:absolute;left:0;top:0;width:8px;height:140px;background:#0b6a6d}

/* footer */
.fcol{top:1088px;font-size:5.8px;color:#2aa7a6;line-height:10.9px}
.fcol h5{font-size:5.8px;color:#137b80;font-weight:700}
.social{top:1092px;width:26px;height:26px;border-radius:50%;background:#138189;display:flex;align-items:center;justify-content:center}
.badge{top:1137px;width:52px;height:18px;background:#111;border-radius:3px}
.rule{left:212px;top:1171px;width:577px;height:1px;background:#e3e3e3}
.copy{left:0;width:1000px;top:1182px;text-align:center;font-size:6px;color:#888}
</style>
</head>
<body>

<header>
  <div class="abs logo"><span class="logo-dot"></span>TuneKiosk</div>
  <nav class="abs nav"><span>About Us</span><span>|</span><span>Contact</span><span>&nbsp;|</span><span>&nbsp;Login</span></nav>
</header>

<section class="abs hero">
  <svg width="205" height="205" viewBox="0 0 205 205">
    <circle cx="94" cy="106" r="100" fill="#fff" opacity=".05"/>
    <circle cx="94" cy="106" r="86" fill="#fff" opacity=".07"/>
    <circle cx="94" cy="106" r="75" fill="#16bfa9"/>
    <path d="M80 78 Q78 72 84 74 L152 108 Q157 112 152 116 L84 150 Q78 152 80 146 Z" fill="#e8f7f4"/>
  </svg>
  <div class="abs hero-title">THE TUNEKIOSK PLATFORM</div>
  <div class="abs hero-sub">Join to save artists, tracks, stations and more.</div>
  <div class="abs join"><i><svg width="10" height="10" viewBox="0 0 10 10"><path d="M0 4h2v6H0zM3 4l2-4c1 0 1.5.6 1.2 1.8L6 4h3c.8 0 1 .6.8 1.2L9 9c-.2.6-.6 1-1.2 1H3z" fill="#fff"/></svg></i>Join Now</div>
</section>

<section class="stations">
  <div class="abs arrow" style="left:278px">‹</div>
  <div class="abs arrow" style="left:715px">›</div>

  <article class="abs card" style="left:288px">
    <div class="art" role="img" aria-label="Album art: brown abstract brush strokes on tan" style="background:linear-gradient(135deg,#e2c39f,#9c7b6a 50%,#dcc0a0)"></div>
    <h3>The Northern Lark</h3><hr>
    <div class="stars">★★★<span class="off">★★</span></div>
  </article>

  <article class="abs card" style="left:396px">
    <div class="art" role="img" aria-label="Album art: soft pale green blurred scene" style="background:linear-gradient(135deg,#dde9e4,#b7cfc8 60%,#e7efec)">
      <svg width="95" height="95" style="position:absolute;left:0;top:0"><circle cx="48" cy="47" r="21" fill="#7f9792" opacity=".85"/><path d="M43 37 L57 47 L43 57Z" fill="#fff"/></svg>
    </div>
    <h3>Quiet Harbor</h3><hr>
    <div class="stars">★★<span class="off">★★★</span></div>
  </article>

  <article class="abs card" style="left:505px">
    <div class="art" role="img" aria-label="Album art: deep blue and purple wave texture" style="background:linear-gradient(160deg,#2a1fa8,#3c2bd0 50%,#1a1480)">
      <div class="mini-player">
        <svg width="103" height="52"><path d="M28 14l-4 2.5 4 2.5zM32 14l-4 2.5 4 2.5z" fill="#fff"/><rect x="46" y="12" width="2" height="8" fill="#fff"/><rect x="51" y="12" width="2" height="8" fill="#fff"/><path d="M68 14l4 2.5-4 2.5zM72 14l4 2.5-4 2.5z" fill="#fff"/><rect x="7" y="31" width="89" height="1.5" fill="#3bbfc0"/><rect x="26" y="28" width="1.5" height="7" fill="#fff"/></svg>
        <span class="label">LITTLE RED CAR</span><span class="time">3:12</span>
      </div>
    </div>
    <h3>Snow Lodge</h3><hr>
    <div class="stars">★★★★<span class="off">★</span></div>
  </article>

  <article class="abs card" style="left:615px">
    <div class="art" role="img" aria-label="Album art: colourful paint strokes on cream" style="background:radial-gradient(circle at 50% 45%,#d86a4c 0%,#2f8b8f 35%,#f0e3da 65%)">
      <svg width="10" height="10" style="position:absolute;left:0;top:0"><path d="M0 0h10L0 10z" fill="#222"/></svg>
    </div>
    <h3>Amber Pines</h3><hr>
    <div class="stars">★★★★★</div>
  </article>
</section>

<section class="abs top3">
  <div class="rank" style="top:0">1</div>
  <div class="track" style="top:0"><div class="thumb" role="img" aria-label="Cover art" style="background:radial-gradient(#d9a77a,#7a4a2c)"></div><b>Moon Fox</b><small>Lira Vance</small><em>593 ♥</em></div>
  <div class="rank" style="top:41px;background:#5fd3d6">2</div>
  <div class="track" style="top:41px"><div class="thumb" role="img" aria-label="Cover art" style="background:radial-gradient(#b06a6a,#3a2228)"></div><b>Open Eyes</b><small>Kara Penn</small><em>412 ♥</em></div>
  <div class="rank" style="top:82px">3</div>
  <div class="track" style="top:82px"><div class="thumb" role="img" aria-label="Cover art" style="background:radial-gradient(#b44a6a,#3c1a2a)"></div><b>Iron Heart</b><small>Bram Moss</small><em>360 ♥</em></div>
  <div class="top3-foot">
    <div class="top3-label">TOP 3</div>
    <div class="tab-btn" style="left:68px;background:#27a6b2"><svg width="9" height="6" style="position:absolute;left:21px;top:8px"><rect width="6" height="6" fill="#fff"/><path d="M6 3l3-3v6z" fill="#fff"/></svg>SHOWS</div>
    <div class="tab-btn" style="left:118px;width:50px;background:#1c909c"><svg width="7" height="8" style="position:absolute;left:22px;top:7px"><path d="M2 0h5v6" stroke="#fff" fill="none"/><circle cx="1.5" cy="6.5" r="1.5" fill="#fff"/><circle cx="5.5" cy="6" r="1.5" fill="#fff"/></svg>BANDS</div>
  </div>
</section>

<section class="abs video" role="img" aria-label="Video still: blurred portrait in pink and mauve tones">
  <div class="video-bar">
    <svg width="242" height="30"><rect x="13" y="11" width="2" height="8" fill="#fff"/><rect x="17" y="11" width="2" height="8" fill="#fff"/><text x="31" y="18" fill="#fff" font-size="7" font-family="Roboto">14:02</text><rect x="54" y="14" width="86" height="1.5" fill="#ddd"/><rect x="137" y="11" width="2" height="7" fill="#fff"/><text x="148" y="18" fill="#fff" font-size="7" font-family="Roboto">19:47</text><path d="M178 12h3l4-3v12l-4-3h-3z" fill="#fff"/><rect x="196" y="14" width="33" height="1.5" fill="#bbb"/><circle cx="211" cy="14.8" r="2.5" fill="#fff"/></svg>
  </div>
</section>

<section class="abs panel">
  <div class="ptab" style="left:0;width:149px;background:#0b6063">
    <svg width="36" height="36" style="top:22px"><circle cx="14" cy="14" r="10" stroke="#fff" stroke-width="4" fill="none"/><path d="M21 21l10 10" stroke="#fff" stroke-width="5" stroke-linecap="round"/></svg>
  </div>
  <div class="ptab" style="left:149px;width:154px;background:#0f7378">
    <svg width="50" height="32"><circle cx="14" cy="11" r="5" fill="#fff"/><circle cx="36" cy="11" r="5" fill="#fff"/><circle cx="25" cy="9" r="6" fill="#fff"/><path d="M4 32c0-8 4-12 10-12s10 4 10 12zM26 32c0-8 4-12 10-12s10 4 10 12z" fill="#fff"/><path d="M13 32c0-10 5-15 12-15s12 5 12 15z" fill="#fff" stroke="#0f7378" stroke-width="1.5"/></svg>
    <span>MY TUNEKIOSK</span>
  </div>
  <div class="ptab" style="left:303px;width:154px;background:#14868b">
    <svg width="40" height="38"><path d="M8 30 L26 6 A18 18 0 0 1 8 30Z" fill="#fff" transform="rotate(15 18 18)"/><circle cx="28" cy="10" r="3" fill="#fff"/><path d="M6 36h22l-6-10h-10z" fill="#fff"/></svg>
    <span>LOCAL STATION</span>
  </div>
  <div class="ptab" style="left:457px;width:153px;background:#1b969c">
    <svg width="28" height="38"><rect x="8" y="0" width="12" height="22" rx="6" fill="#fff"/><path d="M3 16a11 11 0 0 0 22 0" stroke="#fff" stroke-width="2.5" fill="none"/><rect x="12.5" y="27" width="3" height="6" fill="#fff"/><rect x="7" y="33" width="14" height="3" fill="#fff"/></svg>
    <span>MY STATION</span>
  </div>

  <div class="side" style="top:103px">
    <div class="side-head"><i><svg width="8" height="11"><path d="M4 0a4 4 0 0 1 4 4c0 3-4 7-4 7S0 7 0 4a4 4 0 0 1 4-4z" fill="#fff"/><circle cx="4" cy="4" r="1.5" fill="#0f6a70"/></svg></i>Location</div>
    <div class="side-item"><i></i>SHOWS NEAR</div>
    <div class="side-item"><i></i>BANDS FROM</div>
    <div class="side-item"><i></i>VENUES</div>
    <div class="side-btn" style="margin-top:9px">Search Location</div>
    <div class="side-btn">Search Venues</div>
    <div class="side-rule"></div>
    <div class="side-head" style="margin-top:12px"><i><svg width="10" height="10"><path d="M3 1l7-1v7" stroke="#fff" stroke-width="1.5" fill="none"/><circle cx="2" cy="8" r="2" fill="#fff"/><circle cx="8.5" cy="7" r="2" fill="#fff"/></svg></i>Genre</div>
    <div class="side-btn">Search Genre</div>
    <div class="side-rule"></div>
    <div class="side-head" style="margin-top:12px"><i><svg width="7" height="14"><circle cx="3.5" cy="2" r="2" fill="#fff"/><rect x="1" y="5" width="5" height="9" fill="#fff"/></svg></i>Artist</div>
    <div class="side-btn">Search Artist</div>
    <div class="side-rule"></div>
  </div>
  <div class="find">FIND SHOWS</div>

  <div class="gigs">
    <div class="gigs-head"><div class="lead"></div><h4 style="left:41px">BAND NAME</h4><h4 style="left:207px">UPCOMING GIG</h4>
      <svg width="22" height="22" style="position:absolute;left:405px;top:23px"><circle cx="11" cy="11" r="10" fill="#136f78"/><path d="M8 6l8 5-8 5z" fill="#fff"/></svg>
    </div>
    <div class="row" style="top:54px"><span class="star">★</span><b>KVL</b><small>USA</small><b class="gig">21 Mar - Agave Tap Hall</b><small class="gig" style="left:207px">Tempe, AZ, USA</small></div>
    <div class="row" style="top:86.5px"><span class="star">★</span><b>Soft Signal</b><small>USA</small><b class="gig">27 Mar - Boxhall at the Pier</b><small style="left:207px">Seattle, WA, USA</small></div>
    <div class="row" style="top:119px"><span class="star">★</span><b>Outline</b><small>USA</small><b class="gig">28 Mar - Oasis Nightclub</b><small style="left:207px">Miami, FL, USA</small></div>
    <div class="row" style="top:151.5px"><span class="star off">★</span><b>The Ghost Crew</b><small>USA</small><b class="gig">25 Apr - The Alley Electric Chart Room</b><small style="left:207px">New York, NY, USA</small></div>
    <div class="row" style="top:184px"><span class="star off">★</span><b>Basaltino</b><small>USA</small><b class="gig">----------</b></div>
    <div class="row" style="top:216.5px"><span class="star off">★</span><b>Cousins</b><small>USA</small><b class="gig">----------</b></div>
    <div class="row" style="top:249px;height:33px"><span class="star off">★</span><b>Teal Wagon</b><small>USA</small><b class="gig">----------</b></div>
    <div class="scroll"><i></i></div>
  </div>
</section>

<footer>
  <div class="abs fcol" style="left:279px"><h5>ABOUT</h5>TuneKiosk<br>TuneKiosk101<br>Blog<br>Careers<br>Contact Us<br>Concerts by Gigfinder</div>
  <div class="abs fcol" style="left:384px"><h5>SERVICE</h5>Venue and Festival Partners<br>Artist Quick Join<br>Venues<br>Festivals<br>Newspapers<br>API</div>
  <div class="abs social" style="left:609px"><svg width="10" height="7"><rect width="10" height="7" fill="#fff"/><path d="M0 0l5 4 5-4" stroke="#138189" fill="none"/></svg></div>
  <div class="abs social" style="left:641px"><svg width="9" height="9"><circle cx="1.5" cy="7.5" r="1.5" fill="#fff"/><path d="M0 4a5 5 0 0 1 5 5M0 1a8 8 0 0 1 8 8" stroke="#fff" stroke-width="1.5" fill="none"/></svg></div>
  <div class="abs social" style="left:673px"></div>
  <div class="abs social" style="left:706px"></div>
  <div class="abs badge" style="left:611px"></div>
  <div class="abs badge" style="left:680px"></div>
  <div class="abs rule"></div>
  <div class="abs copy">Copyright © 2014 TuneKiosk</div>
</footer>

</body>
</html>
```